Agent Recruiting Package

Redesign of our basic real estate agent recruiting brochure. The design can be several pages long and should incorporate all of the elements in the attached document. Additional information can be added at the designers discretion. Ideally I would like it to be more eye catching so it should probably have more images then the attached design.
The "About Us" should be shortened to the version attached in the word document.
Viewing Clock graphics can be found at http://www.viewingclock-example.com/Resources/GraphicResources.aspx
Ideally final files should be editable by me (someone who does not have access to high end adobe graphic programs). I do have access to Brightleaf Layouter and if the best design is only available in Adobe I will work with it.
Please feel free to submit questions. Also make any changes to design, wording, layout, etc. that you feel make a better overall document.
Target Market(s)
Agents currently working for other real estate borkers and new agents just joining the real estate business
Industry/Entity Type
Real Estate
Look and feel

```html
<!DOCTYPE html>
<html lang="en">
<head>
<meta charset="utf-8">
<title>Notes Spread – Harlan M. Real Estate, LLC</title>
<link rel="stylesheet" href="https://fonts.googleapis.com/css2?family=Oswald:wght@600;700&family=Roboto:wght@400&display=swap">
<style>
  :root {
    --backdrop: #4d4d4d;
    --page-frame: #d4d5d7;
    --sheet: #ffffff;
    --brand-red: #a3303d;
    --rule: #9a9a9a;
    --footer-ink: #555555;
    --folio-ink: #4a4a4a;
  }
  html, body {
    margin: 0;
    padding: 0;
    width: 1200px;
    height: 900px;
    overflow: hidden;
    background: var(--backdrop);
  }
  .spread {
    position: relative;
    width: 1200px;
    height: 900px;
  }
  .page {
    position: absolute;
    top: 82px;
    height: 738px;
    background: var(--page-frame);
  }
  .page--left  { left: 29px;  width: 571px; }
  .page--right { left: 605px; width: 566px; }

  .page__sheet {
    position: absolute;
    top: 14px;
    height: 672px;
    background: var(--sheet);
  }
  .page--left  .page__sheet { left: 13px; width: 546px; }
  .page--right .page__sheet { left: 8px;  width: 545px; }

  .notes__title {
    position: absolute;
    left: 21px;
    top: 8px;
    margin: 0;
    font-family: "Oswald", "Arial Narrow", sans-serif;
    font-weight: 700;
    font-size: 39px;
    line-height: 1.2;
    color: var(--brand-red);
    letter-spacing: 0.2px;
  }
  .notes__lines {
    position: absolute;
    left: 21px;
    top: 75px;
    width: 503px;
    height: 578.3px;
    background-image: repeating-linear-gradient(
      to bottom,
      transparent 0,
      transparent 21.24px,
      var(--rule) 21.24px,
      var(--rule) 22.24px
    );
  }

  .page__footer {
    position: absolute;
    top: 702px;
    display: flex;
    align-items: baseline;
    gap: 9px;
    white-space: nowrap;
  }
  .page--left  .page__footer { left: 34px; }
  .page--right .page__footer { right: 34px; }

  .page__folio {
    font-family: "Oswald", "Arial Narrow", sans-serif;
    font-weight: 600;
    font-size: 16px;
    color: var(--folio-ink);
  }
  .page__company {
    font-family: "Roboto", Arial, sans-serif;
    font-size: 9px;
    letter-spacing: 0.4px;
    color: var(--footer-ink);
  }
</style>
</head>
<body>
  <div class="spread">
    <section class="page page--left">
      <div class="page__sheet">
        <h2 class="notes__title">NOTES</h2>
        <div class="notes__lines"></div>
      </div>
      <footer class="page__footer">
        <span class="page__folio">10</span>
        <span class="page__company">HARLAN M. REAL ESTATE, LLC</span>
      </footer>
    </section>

    <section class="page page--right">
      <div class="page__sheet">
        <h2 class="notes__title">NOTES</h2>
        <div class="notes__lines"></div>
      </div>
      <footer class="page__footer">
        <span class="page__company">HARLAN M. REAL ESTATE, LLC</span>
        <span class="page__folio">11</span>
      </footer>
    </section>
  </div>
</body>
</html>
```